Stylish Business Cards Wanted

- DOUBLE SIDED Design Required -

High end, edgy cards for a corporate and personal stylist. Must include logo,
Name: Belinda Forsey
Title: Director and Stylist
telephone : +61 8 8217 4592
email: belinda@thegarbledger.example
website: thegarbledger.example
Tag: Corporate Workwear & Uniform Specialist | Personal Stylist
Would like nice icons for telephone, email, website

Target Market(s)

Businesses wanting stylish uniforms, people wanting stylish wardrobes

Industry/Entity Type

Corporate Workwear Stylist

Contact Information for Business Card

I would like black, white and gold foiling incorporated in the design - possibly a touch of the other colours on my branding guide attached Name: Belinda Forsey Title: Director and Stylist telephone : +61 8 8217 4592 email: belinda@thegarbledger.example website: thegarbledger.example Tag: Corporate Workwear & Uniform Specialist | Personal Stylist Would like nice icons for telephone, email, website

Font styles to use
Other font styles liked:
• Raleway

Colors

Designer to choose colors to be used in the design.

Requirements
Must have
• Gold foil accents

```html
<!DOCTYPE html>
<html lang="en">
<head>
<meta charset="utf-8">
<title>The Garb Ledger – Business Card</title>
<link href="https://fonts.googleapis.com/css2?family=Raleway:wght@500;600;700&family=Arimo:wght@400&display=swap" rel="stylesheet">
<style>
  :root {
    --page: #2b2b2b;
    --ink: #231f20;
    --ink-soft: #2e2a2b;
    --paper: #ffffff;
    --gold: #e0b547;
    --rule: #cfcfcf;
  }
  * { margin: 0; padding: 0; box-sizing: border-box; }
  html, body { width: 1200px; height: 1015px; overflow: hidden; }
  body {
    background: var(--page);
    font-family: "Arimo", Arial, sans-serif;
    position: relative;
  }
  .card {
    position: absolute;
    left: 215px;
    width: 770px;
    height: 440px;
    overflow: hidden;
  }

  /* Back side */
  .card-back { top: 45px; background: var(--ink); }
  .back-pattern {
    position: absolute; inset: 0;
    background: linear-gradient(135deg, #2a2627 0%, #1f1b1c 50%, #2a2627 100%);
  }
  .back-brand {
    position: absolute; left: 0; right: 0; top: 50%;
    transform: translateY(-50%);
    text-align: center;
    font-family: "Raleway", sans-serif;
    font-weight: 700;
    font-size: 26px;
    letter-spacing: 1px;
    color: var(--paper);
  }

  /* Front side */
  .card-front { top: 530px; background: var(--paper); }
  .front-brand {
    position: absolute; left: 40px; top: 0; width: 270px; height: 348px;
    display: flex; align-items: center; justify-content: center;
    font-family: "Raleway", sans-serif;
    font-weight: 700;
    font-size: 40px;
    line-height: 1.05;
    text-align: center;
    color: var(--ink);
  }
  .divider {
    position: absolute; left: 336px; top: 40px; width: 1px; height: 270px;
    background: linear-gradient(to bottom, transparent, var(--rule) 30%, var(--rule) 70%, transparent);
  }
  .contact-block { position: absolute; left: 380px; top: 60px; }
  .person-name {
    font-family: "Raleway", sans-serif;
    font-weight: 600;
    font-size: 30px;
    color: var(--gold);
    letter-spacing: 0.5px;
    text-transform: uppercase;
  }
  .person-title { font-size: 20px; color: var(--ink); margin-top: 4px; }
  .contact-list { list-style: none; margin-top: 36px; }
  .contact-list li {
    display: flex; align-items: center; gap: 14px;
    font-size: 19px; color: var(--ink); height: 32px;
  }
  .contact-list svg { width: 22px; height: 22px; flex: none; }
  .tag-band {
    position: absolute; left: 0; right: 0; bottom: 0; height: 92px;
    background: var(--ink);
    border-top: 4px solid var(--gold);
    display: flex; align-items: center; justify-content: flex-end;
    padding-right: 44px;
    font-size: 21px; color: var(--paper);
  }
  .tag-dot {
    width: 8px; height: 8px; border-radius: 50%;
    background: var(--gold); margin: 0 16px;
  }
</style>
</head>
<body>

<section class="card card-back">
  <div class="back-pattern" role="img" aria-label="Repeating tone-on-tone brand lettering pattern"></div>
  <div class="back-brand">The Garb Ledger</div>
</section>

<section class="card card-front">
  <div class="front-brand">The Garb<br>Ledger</div>
  <div class="divider"></div>

  <div class="contact-block">
    <div class="person-name">Belinda Forsey</div>
    <div class="person-title">Director and Stylist</div>
    <ul class="contact-list">
      <li>
        <svg viewBox="0 0 24 24" aria-hidden="true"><path fill="var(--gold)" d="M6.6 10.8a15.1 15.1 0 0 0 6.6 6.6l2.2-2.2a1 1 0 0 1 1-.25 11.4 11.4 0 0 0 3.6.57 1 1 0 0 1 1 1V20a1 1 0 0 1-1 1A17 17 0 0 1 3 4a1 1 0 0 1 1-1h3.5a1 1 0 0 1 1 1c0 1.25.2 2.45.57 3.57a1 1 0 0 1-.25 1z"/></svg>
        +61 8 8217 4592
      </li>
      <li>
        <svg viewBox="0 0 24 24" aria-hidden="true"><rect x="2" y="5" width="20" height="14" rx="1" fill="var(--gold)"/><path d="M2.5 5.5 12 13l9.5-7.5" fill="none" stroke="#fff" stroke-width="1.6"/></svg>
        belinda@thegarbledger.example
      </li>
      <li>
        <svg viewBox="0 0 24 24" aria-hidden="true"><g fill="none" stroke="var(--gold)" stroke-width="1.8"><circle cx="12" cy="12" r="9.5"/><ellipse cx="12" cy="12" rx="4" ry="9.5"/><path d="M2.5 12h19M4 7h16M4 17h16"/></g></svg>
        thegarbledger.example
      </li>
    </ul>
  </div>

  <div class="tag-band">
    <span>Corporate Workwear &amp; Uniform Specialist</span>
    <span class="tag-dot"></span>
    <span>Personal Stylist</span>
  </div>
</section>

</body>
</html>
```